Album Artwork for Re-Release of Original Country Music CD "Amber Hollow"

I need a fresh CD cover design for my album "Amber Hollow".

This is a re-release on an older project, and I am looking for album artwork that inspires hope in the midst of sorrow.

I am uploading the backside that I had begun to create - I felt this was a nice concept, as the small group of trees in the midst of the storm that were together had a beam of light shining upon them, which spoke hope to me in the midst of sorrow.

I have also uploaded the original front album artwork. It wasn't that it was bad, but I don't have access to the original files, so I am seeking for a fresh start.

I don't yet have a concept for the cover of the CD itself, but I assume that we would use a derivative work from the front cover that would be designed.

The submissions do not have to mirror my ideas, but I hope my ideas convey the general concepts I want this album imagery to convey.

Here are links to listen to the tracks, if you want to get a feel for the general sounds of the album:

Tunevale - https://play.tunevale-example.com/album/7pWqR28MbXnA3GhJKzeoTy

Target Market(s)

Country Music, Ages 25-55

Font styles to use
Other font styles liked:
• The font on the back imagery is Sveningsson. It doesn't have to be that font - just something that captures the spirit of the album.

Colors

Designer to choose colors to be used in the design.

Requirements
Must have
• My name on the front of the album, as well as the album title.
• On the back, it must list the information provided in the picture I uploaded of what I was creating for the back of the album.
Nice to have
• I prefer fonts that encapture the spirit of the album concept. This album has many somber songs within it, so the fonts and the color patterns that are chosen should reflect a spirit of hope in the midst of suffering (or despair).
Should not have
• Happy imagery is obviously not a part of this project. I want it to retain a somber feel, yet still be appealing to the eye of any buyer.

```html
<!DOCTYPE html>
<html lang="en">
<head>
<meta charset="utf-8">
<title>Amber Hollow – Wade Carrow</title>
<link rel="stylesheet" href="https://fonts.googleapis.com/css2?family=Anton&family=Montserrat:wght@500&display=swap">
<style>
  :root {
    --amber: #e3a43a;
    --gold: #f4c743;
    --ochre: #b8801e;
    --teal: #22c3cf;
    --sea: #0f6a72;
    --moss: #6d8f2e;
    --violet: #8c3a9c;
    --umber: #2e1a0a;
    --ink: #000000;
    --paper: #ffffff;
  }
  html, body {
    margin: 0;
    padding: 0;
    width: 1200px;
    height: 1200px;
    overflow: hidden;
    background: var(--umber);
  }
  .cover {
    position: relative;
    width: 1200px;
    height: 1200px;
    overflow: hidden;
  }
  .cover-art, .title-mark, .artist-mark {
    position: absolute;
    inset: 0;
    width: 1200px;
    height: 1200px;
  }
  .album-title {
    font-family: "Anton", "Impact", sans-serif;
    font-size: 158px;
    fill: var(--ink);
    stroke: var(--paper);
    stroke-width: 8px;
    paint-order: stroke fill;
    stroke-linejoin: round;
  }
  .artist-letter {
    font-family: "Montserrat", "Arial", sans-serif;
    font-weight: 500;
    font-size: 88px;
    fill: var(--paper);
    stroke: var(--ink);
    stroke-width: 6px;
    paint-order: stroke fill;
    text-anchor: middle;
  }
</style>
</head>
<body>
  <main class="cover">
    <svg class="cover-art" viewBox="0 0 1200 1200" role="img" aria-label="Stormy abstract collage of cracked amber, teal and violet textures with faint sheet music lines">
      <defs>
        <radialGradient id="amber-glow" cx="0.15" cy="0.3" r="0.55">
          <stop offset="0" stop-color="var(--amber)"/>
          <stop offset="1" stop-color="var(--ochre)" stop-opacity="0"/>
        </radialGradient>
        <radialGradient id="gold-glow" cx="0.9" cy="0.1" r="0.4">
          <stop offset="0" stop-color="var(--gold)"/>
          <stop offset="1" stop-color="var(--gold)" stop-opacity="0"/>
        </radialGradient>
        <linearGradient id="teal-block" x1="0" y1="0" x2="1" y2="1">
          <stop offset="0" stop-color="var(--moss)"/>
          <stop offset="0.45" stop-color="var(--teal)"/>
          <stop offset="1" stop-color="var(--sea)"/>
        </linearGradient>
        <radialGradient id="violet-glow" cx="0.1" cy="0.72" r="0.35">
          <stop offset="0" stop-color="var(--violet)"/>
          <stop offset="1" stop-color="var(--violet)" stop-opacity="0"/>
        </radialGradient>
        <linearGradient id="gold-streak" x1="0" y1="0" x2="1" y2="1">
          <stop offset="0" stop-color="var(--gold)" stop-opacity="0.9"/>
          <stop offset="1" stop-color="var(--ochre)" stop-opacity="0.3"/>
        </linearGradient>
        <radialGradient id="vignette" cx="0.5" cy="0.5" r="0.75">
          <stop offset="0.6" stop-color="#000" stop-opacity="0"/>
          <stop offset="1" stop-color="#000" stop-opacity="0.5"/>
        </radialGradient>
      </defs>

      <rect class="base" width="1200" height="1200" fill="var(--umber)"/>
      <rect class="amber-field" width="1200" height="1200" fill="url(#amber-glow)"/>
      <rect class="gold-field" width="1200" height="1200" fill="url(#gold-glow)"/>

      <polygon class="teal-panel" points="420,150 1200,150 1200,1090 700,1090 430,760" fill="url(#teal-block)" opacity="0.9"/>
      <polygon class="shadow-wedge" points="340,0 470,0 620,520 180,560 0,640 0,560 220,470" fill="var(--umber)" opacity="0.8"/>
      <polygon class="gold-streak" points="330,0 560,0 1000,1200 830,1200" fill="url(#gold-streak)" opacity="0.55"/>
      <polygon class="gold-streak-right" points="1080,0 1200,0 1200,620" fill="var(--gold)" opacity="0.45"/>
      <rect class="violet-field" width="1200" height="1200" fill="url(#violet-glow)"/>
      <polygon class="dark-corner" points="820,1040 1200,1000 1200,1200 880,1200" fill="var(--umber)" opacity="0.75"/>

      <g class="staff-lines" stroke="var(--paper)" stroke-opacity="0.18" stroke-width="1.5">
        <line x1="0" y1="160" x2="1200" y2="160"/>
        <line x1="0" y1="172" x2="1200" y2="172"/>
        <line x1="0" y1="184" x2="1200" y2="184"/>
        <line x1="0" y1="196" x2="1200" y2="196"/>
        <line x1="0" y1="208" x2="1200" y2="208"/>
        <line x1="420" y1="740" x2="1200" y2="740"/>
        <line x1="420" y1="752" x2="1200" y2="752"/>
        <line x1="420" y1="764" x2="1200" y2="764"/>
        <line x1="420" y1="776" x2="1200" y2="776"/>
        <line x1="420" y1="788" x2="1200" y2="788"/>
      </g>
      <line class="ember-line" x1="240" y1="1125" x2="640" y2="1125" stroke="#e0452a" stroke-opacity="0.6" stroke-width="3"/>
      <line class="ember-line" x1="560" y1="70" x2="1120" y2="70" stroke="#e0452a" stroke-opacity="0.4" stroke-width="2"/>
      <rect class="vignette" width="1200" height="1200" fill="url(#vignette)"/>
    </svg>

    <svg class="title-mark" viewBox="0 0 1200 1200" aria-label="Amber Hollow">
      <text class="album-title" x="166" y="580" textLength="486" lengthAdjust="spacingAndGlyphs">Amber</text>
      <text class="album-title" x="286" y="722" textLength="400" lengthAdjust="spacingAndGlyphs">Hollow</text>
    </svg>

    <svg class="artist-mark" viewBox="0 0 1200 1200" aria-label="Wade Carrow">
      <text class="artist-letter" x="992" y="206">W</text>
      <text class="artist-letter" x="992" y="301">A</text>
      <text class="artist-letter" x="992" y="396">D</text>
      <text class="artist-letter" x="992" y="491">E</text>
      <text class="artist-letter" x="992" y="586">C</text>
      <text class="artist-letter" x="992" y="681">A</text>
      <text class="artist-letter" x="992" y="776">R</text>
      <text class="artist-letter" x="992" y="871">R</text>
      <text class="artist-letter" x="992" y="966">O</text>
      <text class="artist-letter" x="992" y="1061">W</text>
    </svg>
  </main>
</body>
</html>
```